A boutique/architectural website for a landscape company

I'm after a minimilstic boutique website for my landscape design and construction business. I have been exploring Wix and created some pages on that but want something more aesthetic.

Industry/Entity Type

Landscaping design and construction

Number of Pages Required

5+ page

Font styles to use
Sans Serif

Colors

Designer to choose colors to be used in the design.

Requirements
Must have
• an architectural, minimalistic look
Nice to have
• Simplicitly and nice images
Should not have
• A corporate look

```html
<!DOCTYPE html>
<html lang="en">
<head>
<meta charset="utf-8">
<title>Verdale — Landscaping &amp; Design</title>
<link rel="stylesheet" href="https://fonts.googleapis.com/css2?family=Montserrat:wght@400;600;700;800&family=Raleway:wght@300;400;500&family=Roboto+Condensed:wght@700&display=swap">
<style>
:root{
  --green:#2f9a1c;
  --green-dark:#268414;
  --ink:#2b2f36;
  --muted:#6f747b;
  --soft:#f5f6f8;
  --line:#e4e6ea;
  --white:#ffffff;
  --footer:#232427;
}
*{box-sizing:border-box;margin:0;padding:0}
html,body{width:1200px;height:3416px;overflow:hidden}
body{font-family:"Raleway",sans-serif;color:var(--ink);background:var(--white);position:relative}
section,header,footer{position:absolute;left:0;width:1200px}
.center{text-align:center}

/* hero */
.hero{top:0;height:639px;overflow:hidden}
.hero-half{position:absolute;top:0;height:639px}
.hero-left{left:0;width:602px;background:linear-gradient(180deg,#4a3a2a 0%,#6a4a2a 18%,#2f3a22 45%,#2c4a16 70%,#1c2a0e 100%)}
.hero-right{left:602px;width:598px;background:linear-gradient(160deg,#3a4650 0%,#5a6a78 40%,#4a5866 70%,#3a4450 100%)}
.hero-half::after{content:"";position:absolute;inset:0;background:rgba(0,0,0,.25)}
.nav{position:absolute;top:18px;left:0;width:1200px;height:40px;z-index:2}
.brand{position:absolute;left:162px;top:6px;color:var(--white);font-family:"Raleway",sans-serif;font-weight:400;font-size:24px;letter-spacing:4px;display:flex;align-items:center;gap:10px}
.brand-mark{width:12px;height:12px;border-radius:50%;background:var(--white)}
.menu{position:absolute;right:162px;top:4px;display:flex;gap:28px;list-style:none}
.menu li{color:var(--white);font-family:"Raleway",sans-serif;font-size:10px;text-transform:uppercase}
.hero-copy{position:absolute;top:228px;width:420px;color:var(--white);z-index:2}
.hero-copy.left{left:162px}
.hero-copy.right{left:640px}
.hero-copy h1{font-family:"Montserrat",sans-serif;font-weight:800;font-size:42px;line-height:42px}
.hero-copy h2{font-family:"Raleway",sans-serif;font-weight:400;font-size:23px;letter-spacing:.5px;margin-top:2px}
.hero-copy .rule{width:50px;height:4px;background:var(--white);margin:20px 0 25px}
.hero-copy p{font-size:13px;line-height:26px}
.dots{position:absolute;left:613px;top:292px;z-index:2;display:flex;flex-direction:column;gap:9px}
.dots span{width:5px;height:5px;border-radius:50%;background:var(--white)}
.dots span.on{background:var(--green)}
.down{position:absolute;left:589px;top:577px;width:26px;height:26px;background:var(--white);transform:rotate(45deg);z-index:2}
.down svg{transform:rotate(-45deg);position:absolute;left:6px;top:6px}

/* intro */
.intro{top:639px;height:326px;background:var(--soft)}
.section-title{font-family:"Montserrat",sans-serif;font-weight:600;font-size:23px;letter-spacing:4px;color:var(--ink)}
.title-rule{width:92px;height:2px;background:var(--green);margin:0 auto}
.intro .section-title{margin-top:62px}
.intro .title-rule{margin-top:14px}
.intro p{width:670px;margin:40px auto 0;font-size:13px;line-height:22.5px;color:var(--muted)}

/* services */
.services{top:965px;height:659px;background:var(--white)}
.focus{position:absolute;left:162px;top:115px}
.focus h2{font-family:"Montserrat",sans-serif;font-weight:700;font-size:38px;line-height:40px;color:#3a3d43}
.focus h3{font-family:"Montserrat",sans-serif;font-weight:600;font-size:22px;color:#3a3d43;margin-top:2px}
.focus p{font-family:"Raleway",sans-serif;font-size:11px;color:var(--ink);margin-top:30px}
.tile{position:absolute;width:202px;height:126px;border:1px solid var(--line);background:var(--white);display:flex;flex-direction:column;align-items:center;justify-content:center;gap:10px}
.tile span{font-family:"Roboto Condensed",sans-serif;font-weight:700;font-size:11px;color:#33363b;text-transform:uppercase}
.tile.active .inner{position:absolute;inset:7px;background:var(--green);display:flex;flex-direction:column;align-items:center;justify-content:center;gap:10px}
.tile.active span{color:var(--white)}
.btn{background:var(--green);color:var(--white);font-family:"Montserrat",sans-serif;font-size:9px;letter-spacing:2px;padding:14px 22px;text-transform:uppercase}

/* portfolio */
.portfolio{top:1624px;height:581px;background:var(--soft);overflow:hidden}
.portfolio .section-title{margin-top:60px;letter-spacing:0;font-size:22px;font-weight:700}
.portfolio .title-rule{margin-top:12px}
.portfolio .lead{width:720px;margin:18px auto 0;font-size:12.5px;line-height:17px;color:var(--muted)}
.filters{display:flex;justify-content:center;gap:0;margin-top:36px;list-style:none}
.filters li{font-family:"Raleway",sans-serif;font-size:12px;padding:8px 18px;color:var(--ink);text-transform:uppercase;border:1px solid transparent;margin:0 2px}
.filters li.on{border-color:var(--green)}
.cards{position:absolute;top:251px;left:-154px;display:flex;gap:6px}
.card{width:295px;height:292px;background:var(--white)}
.card .photo{height:188px;position:relative}
.card h4{font-family:"Montserrat",sans-serif;font-weight:600;font-size:10px;color:var(--green);text-align:center;margin-top:20px;text-transform:uppercase}
.card .rule{width:34px;height:1px;background:var(--green);margin:8px auto 0}
.card p{font-size:10px;color:var(--muted);text-align:center;width:170px;margin:14px auto 0;line-height:13px}
.plus{position:absolute;left:120px;top:67px;width:54px;height:54px;border-radius:50%;background:rgba(255,255,255,.9)}

/* video */
.video{top:2205px;height:398px;background:linear-gradient(180deg,#3c3a30 0%,#4a4232 45%,#3a3428 75%,#2a2822 100%);color:var(--white)}
.video::after{content:"";position:absolute;inset:0;background:rgba(0,0,0,.2)}
.video .wrap{position:relative;z-index:1}
.video h2{font-family:"Montserrat",sans-serif;font-weight:700;font-size:22px;margin-top:128px}
.video .title-rule{margin-top:10px;width:200px}
.video p{width:720px;margin:18px auto 0;font-size:12.5px;line-height:17px}
.video .see{margin-top:24px;font-size:13px}
.play{margin:8px auto 0;width:27px;height:27px;border:1.5px solid var(--white);border-radius:50%;display:flex;align-items:center;justify-content:center}

/* stats */
.stats{top:2603px;height:216px;background:var(--green);color:var(--white)}
.stat{position:absolute;top:52px;width:200px;margin-left:-100px;text-align:center}
.stat .num{font-family:"Montserrat",sans-serif;font-weight:600;font-size:37px;line-height:40px;margin-top:14px}
.stat .label{font-family:"Montserrat",sans-serif;font-weight:600;font-size:12px;margin-top:6px;text-transform:uppercase}

/* contact */
.contact{top:2819px;height:505px;background:var(--soft)}
.contact .section-title{margin-top:84px;font-size:22px}
.divider{position:relative;width:420px;height:14px;margin:14px auto 0}
.divider::before,.divider::after{content:"";position:absolute;top:4px;width:182px;border-top:1px dotted #c6c9cd}
.divider::before{left:0}.divider::after{right:0}
.divider svg{position:absolute;left:204px;top:0}
.info{position:absolute;top:204px;width:270px;height:112px;background:var(--white);text-align:center;padding-top:24px}
.info h5{font-family:"Montserrat",sans-serif;font-weight:600;font-size:13px;letter-spacing:2px;color:var(--green);margin-top:6px}
.info p{font-size:12.5px;color:var(--ink);margin-top:14px}
.socials{position:absolute;top:389px;left:538px;display:flex;gap:15px}
.socials span{width:30px;height:30px;border-radius:50%;background:var(--ink)}
.socials span.on{background:var(--green)}

/* footer */
footer{top:3324px;height:92px;background:var(--footer);color:#bfc2c7;font-size:12.5px}
footer .legal{position:absolute;left:172px;top:37px}
footer .credit{position:absolute;right:174px;top:37px}
footer .credit em{color:var(--green);font-style:normal}
</style>
</head>
<body>

<header class="hero">
  <div class="hero-half hero-left" role="img" aria-label="Photo of terraced green rice fields below misty mountains at sunset"></div>
  <div class="hero-half hero-right" role="img" aria-label="Photo of a builder in a yellow hard hat holding plans at a construction site"></div>
  <nav class="nav">
    <div class="brand"><span class="brand-mark"></span>VERDALE</div>
    <ul class="menu"><li>Home</li><li>Works</li><li>Industries</li><li>Services</li><li>Who we are</li><li>Contact</li></ul>
  </nav>
  <div class="hero-copy left">
    <h1>WHERE THE</h1>
    <h2>LANDSCAPE REFLECT PERFECTION</h2>
    <div class="rule"></div>
    <p>Maecenas suscipit imperdiet nisi ac hendrerit. Nam congue felis ac massa rutrum pulvinar. Donec sodales eros sed efficitur mattis. Integer tincidunt, felis a placerat maximus, eros nulla dapibus dui, at facilisis enim .</p>
  </div>
  <div class="hero-copy right">
    <h1>THE BEST</h1>
    <h2>SOLUTIONS FOR YOUR BUSINESS</h2>
    <div class="rule"></div>
    <p>Maecenas suscipit imperdiet nisi ac hendrerit. Nam congue felis ac massa rutrum pulvinar. Donec sodales eros sed efficitur mattis. Integer tincidunt, felis a placerat maximus, eros nulla dapibus dui, at facilisis enim .</p>
  </div>
  <div class="dots"><span></span><span class="on"></span><span></span><span></span></div>
  <div class="down"><svg width="14" height="14" viewBox="0 0 14 14"><path d="M3 5l4 4 4-4" fill="none" stroke="#2b2f36" stroke-width="2"/></svg></div>
</header>

<section class="intro center">
  <h2 class="section-title">HOW WE ARE</h2>
  <div class="title-rule"></div>
  <p>Sed a lorem quis neque interdum consequat ut sed sem. Duis quis tempor nunc. Interdum et malesuada fames ac ante ipsum primis in faucibus. Praesent id tempor ipsum. Fusce at massa ac nunc porta fringilla sed eget neque. Quisque quis pretium nulla. Fusce eget bibendum neque, vel volutpat augue. Lorem ipsum dolor sit amet, consectetur adipiscing elit. Interdum et malesuada fames ac ante ipsum primis in faucibus.</p>
</section>

<section class="services">
  <div class="focus">
    <h2>WE FOCUS</h2>
    <h3>ON KEY SERVICES OF LANDSCAPE</h3>
    <p>Donec nulla justo, pharetra in nulla in, lacinia pulvinar nunc rutrum nisi vel nib.</p>
  </div>
  <div class="tile" style="left:611px;top:113px"><svg width="34" height="30" viewBox="0 0 34 30" fill="none" stroke="#33363b" stroke-width="1.4"><path d="M4 8c6-4 12-4 20 0M6 13c5-3 11-3 18 0"/><path d="M8 26l2-8 2 8 2-8 2 8 2-8 2 8 2-8 2 8"/></svg><span>Lawn Maintenance</span></div>
  <div class="tile" style="left:837px;top:113px"><svg width="26" height="32" viewBox="0 0 26 32" fill="none" stroke="#33363b" stroke-width="1.4"><rect x="4" y="5" width="18" height="25" rx="2"/><path d="M7 2h12"/><circle cx="13" cy="17" r="5"/></svg><span>Fertilization &amp; Weed Control</span></div>
  <div class="tile" style="left:162px;top:263px"><svg width="42" height="34" viewBox="0 0 42 34" fill="none" stroke="#33363b" stroke-width="1.4"><path d="M4 4l12 16"/><rect x="14" y="18" width="20" height="8" rx="3"/><circle cx="18" cy="29" r="3"/><circle cx="32" cy="29" r="3"/></svg><span>Landscape Maintenacne</span></div>
  <div class="tile" style="left:386px;top:263px"><svg width="36" height="34" viewBox="0 0 36 34" fill="none" stroke="#33363b" stroke-width="1.4"><path d="M9 20a7 7 0 0 1 2-13 9 9 0 0 1 16 3 5 5 0 0 1 0 10z"/><path d="M18 10v10M13 15h10M14 11l8 8M22 11l-8 8"/><path d="M10 26v2M18 28v2M26 26v2"/></svg><span>Snow and Ice Control</span></div>
  <div class="tile" style="left:611px;top:263px"><svg width="36" height="34" viewBox="0 0 36 34" fill="none" stroke="#33363b" stroke-width="1.4"><path d="M4 12l12-8 10 12-12 8z"/><circle cx="15" cy="14" r="3"/><path d="M28 22l2 2M30 27l3 1M25 28l1 3"/></svg><span>Sod &amp; Seed Installation</span></div>
  <div class="tile" style="left:837px;top:263px"><svg width="34" height="32" viewBox="0 0 34 32" fill="none" stroke="#33363b" stroke-width="1.4"><path d="M17 2l13 24H4z"/><path d="M17 2l-4 24M17 2l6 16 7 8"/></svg><span>Natural Stone Installation</span></div>
  <div class="tile active" style="left:162px;top:413px"><div class="inner"><svg width="32" height="32" viewBox="0 0 32 32" fill="none" stroke="#fff" stroke-width="1.4"><circle cx="16" cy="16" r="14"/><circle cx="16" cy="16" r="9"/><circle cx="16" cy="16" r="3"/><path d="M16 7v18M7 16h18M10 10l12 12M22 10L10 22"/></svg><span>Grading &amp; Drainage</span></div></div>
  <div class="tile" style="left:386px;top:413px"><svg width="26" height="34" viewBox="0 0 26 34" fill="none" stroke="#33363b" stroke-width="1.4"><path d="M8 22c0-4-5-6-5-12a10 10 0 0 1 20 0c0 6-5 8-5 12z"/><path d="M9 26h8M10 30h6"/></svg><span>Lighting Installation</span></div>
  <div class="tile" style="left:611px;top:413px"><svg width="36" height="34" viewBox="0 0 36 34" fill="none" stroke="#33363b" stroke-width="1.4"><rect x="4" y="24" width="12" height="6"/><rect x="18" y="24" width="12" height="6"/><rect x="11" y="17" width="12" height="6"/><rect x="25" y="17" width="8" height="6"/><path d="M6 4l10 6-3 3z"/></svg><span>Brick Pavers</span></div>
  <div class="tile" style="left:837px;top:413px"><div class="btn">Show All</div></div>
</section>

<section class="portfolio center">
  <h2 class="section-title">OUR PORTFOLIO</h2>
  <div class="title-rule"></div>
  <p class="lead">Eum cu tantas legere complectitur, hinc utamur ea eam. Eum patrioque mnesarchum eu, diam erant convenire et vis. Et essent evertitur sea, vis cu ubique referrentur, sed eu dicant expetendis.</p>
  <ul class="filters"><li class="on">All</li><li>Landscape</li><li>Construction</li><li>Maintanince</li></ul>
  <div class="cards">
    <article class="card"><div class="photo" role="img" aria-label="Photo of construction workers in safety vests on site" style="background:linear-gradient(160deg,#8a8c88,#b3ad9e 50%,#6e6a60)"></div><h4>Awesome Photo</h4><div class="rule"></div><p>Eum cu tantas legere complecti-tur, hinc utamu</p></article>
    <article class="card"><div class="photo" role="img" aria-label="Photo of a green meadow with a tree and country road under blue sky" style="background:linear-gradient(180deg,#5f8fc8 0%,#a9c6e2 40%,#6f9e3a 62%,#3e6d1e 100%)"></div><h4>Awesome Photo</h4><div class="rule"></div><p>Eum cu tantas legere complecti-tur, hinc utamu</p></article>
    <article class="card"><div class="photo" role="img" aria-label="Photo of a yellow excavator digging under a cloudy sky" style="background:linear-gradient(180deg,#9a9c9e 0%,#c4c4c0 40%,#b99a2c 62%,#6a6458 100%)"><div class="plus"><svg width="54" height="54" viewBox="0 0 54 54"><path d="M27 15v24M15 27h24" stroke="#c9c9c9" stroke-width="1.5"/></svg></div></div><h4>Awesome Photo</h4><div class="rule"></div><p>Eum cu tantas legere complecti-tur, hinc utamu</p></article>
    <article class="card"><div class="photo" role="img" aria-label="Photo of a modern glass house with scaffolding and blue facade" style="background:linear-gradient(160deg,#8ea3c0,#4a5c88 55%,#3b4660)"></div><h4>Awesome Photo</h4><div class="rule"></div><p>Eum cu tantas legere complecti-tur, hinc utamu</p></article>
    <article class="card"><div class="photo" role="img" aria-label="Photo of an excavator at dusk on a dirt site" style="background:linear-gradient(180deg,#5a6e88 0%,#a0845a 50%,#6a4e30 100%)"></div><h4>Awesome Photo</h4><div class="rule"></div><p>Eum cu tantas legere complecti-tur, hinc utamu</p></article>
  </div>
</section>

<section class="video center" role="img" aria-label="Background photo of an excavator on earthworks at sunset">
  <div class="wrap">
    <h2>NOTHING SAY BETTER,THEN A VIDEO</h2>
    <div class="title-rule"></div>
    <p>Eum cu tantas legere complectitur, hinc utamur ea eam. Eum patrioque mnesarchum eu, diam erant convenire et vis. Et essent evertitur sea, vis cu ubique referrentur, sed eu dicant expetendis.</p>
    <div class="see">See Video</div>
    <div class="play"><svg width="8" height="8" viewBox="0 0 8 8"><path d="M2 1l5 3-5 3z" fill="#fff"/></svg></div>
  </div>
</section>

<section class="stats">
  <div class="stat" style="left:334px"><svg width="44" height="36" viewBox="0 0 44 36" fill="none" stroke="#fff" stroke-width="1.6"><rect x="2" y="8" width="40" height="26"/><path d="M15 8V3h14v5M2 18h40"/></svg><div class="num">3054</div><div class="label">Completed Projects</div></div>
  <div class="stat" style="left:522px"><svg width="26" height="40" viewBox="0 0 26 40" fill="none" stroke="#fff" stroke-width="1.6"><rect x="4" y="10" width="18" height="28" rx="9"/><path d="M13 10v8M13 10C13 4 8 4 8 1"/></svg><div class="num">7 234</div><div class="label">Click Presed</div></div>
  <div class="stat" style="left:709px"><svg width="40" height="40" viewBox="0 0 40 40" fill="none" stroke="#fff" stroke-width="1.6"><path d="M4 16l16-12 16 12v22H4z"/><path d="M4 16l16 12 16-12M4 38l12-12M36 38L24 26"/></svg><div class="num">4670</div><div class="label">Mails Sented &amp; Recived</div></div>
  <div class="stat" style="left:898px"><svg width="40" height="38" viewBox="0 0 40 38" fill="none" stroke="#fff" stroke-width="1.6"><path d="M3 3h34v24H16l-8 8v-8H3z"/><circle cx="13" cy="15" r="1.5"/><circle cx="20" cy="15" r="1.5"/><circle cx="27" cy="15" r="1.5"/></svg><div class="num">939</div><div class="label">Upcomming</div></div>
</section>

<section class="contact center">
  <h2 class="section-title">DROP US A LINE</h2>
  <div class="divider"><svg width="12" height="10" viewBox="0 0 12 10"><path d="M1 1h10L6 9z" fill="#2b2f36"/></svg></div>
  <div class="info" style="left:172px"><svg width="10" height="14" viewBox="0 0 10 14"><path d="M5 13S1 8 1 5a4 4 0 0 1 8 0c0 3-4 8-4 8z" fill="#2b2f36"/><circle cx="5" cy="5" r="1.5" fill="#fff"/></svg><h5>ADDRESS</h5><p>Level 4, 18 Harbour Lane, Brookvale</p></div>
  <div class="info" style="left:464px"><svg width="8" height="14" viewBox="0 0 8 14"><rect x="1" y="1" width="6" height="12" rx="1" fill="none" stroke="#2b2f36" stroke-width="1.6"/><path d="M3 11h2" stroke="#2b2f36"/></svg><h5>PHONE</h5><p>+61 2 5550 0142</p></div>
  <div class="info" style="left:756px"><svg width="12" height="12" viewBox="0 0 12 12"><path d="M1 6l10-5-4 10-1-4z" fill="#2b2f36"/></svg><h5>EMAIL</h5><p>hello@verdale.example</p></div>
  <div class="socials"><span></span><span class="on"></span><span></span></div>
</section>

<footer>
  <div class="legal">Terms &amp; Conditions &nbsp;|&nbsp; Legals</div>
  <div class="credit">Designed &amp; Developed by <em>Fernwork</em> exclusively for VERDALE</div>
</footer>

</body>
</html>
```